Mix Comet business cards + chance to win packaging and other design projects

including logo already designed.

******** I need 2 business cards:
1. that is general for the company
2. that is specific for me

*********On the reverse side of the business card I want it to be divided into 4 boxes and each box to describe a stage in how to use the product. I need the boxes to be numbered and the contents to be easy to absorb and include graphics showing the actions also.
Turning then photo's into simplified, cool illustrations** would be really cool. This would allow changes, like writing "water" on the bottle etc etc. Maybe have a fftness lady drinking at the end? Imagination over to you.
The photo's are of the prototype so the illustrations can replace the grey caps with bright orange etc etc

CAPTIONS FOR ILLUSTRATIONS
1. Charge the Mix Comet
2.The Mix Comet is now ready for making a shake anywhere, anytime !
3. Choose any bottled water or beverage, release shot cap and Jet powder in.
4. Shake bottle, enjoy!
Updates

Can you illustrate?
I just changed the photos and captions to simplify.
Please re read the brief, thanks

Target Market(s)

Fitness, weight loss, health
male and female
any potential powdered drink user.

quince, skyroam design style ? Clean, simple, bold, clever, cool

Industry/Entity Type

Business

Requirements
Must have
• Must have logo and mixcomet.com

Card 1: email: info@mixcomet.com

Card 2: Rafe Dunmore LL.b. /President/ email:rafe@mixcomet.com/ office: 415 382 6619/ direct: 628 741 3085

I want the card to have a white background, not color blocked in.

I have included photos of the type of illustrations needed in each box.
In the illustrations pls make the mix comet army green and the caps bright orange.
Get the point across as simply as you can. Make it cool pls :)

```html
<!DOCTYPE html>
<html lang="en">
<head>
<meta charset="utf-8">
<title>Mix Comet Business Cards</title>
<link rel="stylesheet" href="https://fonts.googleapis.com/css2?family=Open+Sans:ital,wght@0,400;0,600;0,700;0,800;1,400;1,700&display=swap">
<style>
  :root {
    --backdrop: #e8e2d8;
    --card: #ffffff;
    --orange: #f07b1a;
    --blue: #1d4f9c;
    --ink: #3a3a3a;
    --muted: #6d6d6d;
    --photo-skin: #d9b79a;
    --photo-wall: #cfd5dc;
    --photo-green: #6b7a3c;
    --photo-amber: #b98a52;
  }
  * { box-sizing: border-box; margin: 0; padding: 0; }
  html, body { width: 766px; height: 1200px; overflow: hidden; }
  body {
    background: var(--backdrop);
    font-family: "Open Sans", Arial, sans-serif;
    position: relative;
  }
  .card {
    position: absolute;
    left: 97px;
    width: 572px;
    background: var(--card);
    box-shadow: 0 3px 10px rgba(0,0,0,0.18);
  }
  /* Steps card */
  .card--steps { top: 56px; height: 340px; padding: 8px; }
  .steps {
    display: grid;
    grid-template-columns: 1fr 1fr;
    grid-template-rows: 1fr 1fr;
    gap: 6px;
    height: 100%;
  }
  .step { display: flex; flex-direction: column; }
  .step__art {
    position: relative;
    flex: 1;
  }
  .step__art--drink { background: linear-gradient(135deg, var(--photo-wall), var(--photo-skin)); }
  .step__art--charge { background: linear-gradient(135deg, #e8e6e1, var(--photo-green)); }
  .step__art--release { background: linear-gradient(135deg, #d8d8d4, var(--photo-amber)); }
  .step__art--shake { background: linear-gradient(135deg, var(--photo-skin), var(--photo-green)); }
  .step__num {
    position: absolute;
    top: 0; left: 0;
    width: 28px; height: 28px;
    background: var(--orange);
    color: #fff;
    font-weight: 700;
    font-size: 16px;
    display: flex; align-items: center; justify-content: center;
  }
  .step__caption {
    height: 40px;
    display: flex; align-items: center; justify-content: center;
    text-align: center;
    font-size: 10.5px;
    line-height: 1.3;
    color: var(--ink);
    padding: 0 10px;
  }
  /* Shared logo */
  .logo {
    position: absolute;
    display: flex;
    align-items: center;
    gap: 10px;
  }
  .logo__dot {
    width: 14px; height: 14px;
    border-radius: 50%;
    background: var(--orange);
  }
  .logo__name {
    font-weight: 800;
    font-size: 38px;
    letter-spacing: 0.5px;
    color: var(--orange);
    text-transform: uppercase;
  }
  /* General card */
  .card--general { top: 421px; height: 327px; }
  .card--general .logo { left: 34px; top: 52px; }
  .general__phone {
    position: absolute;
    left: 332px; top: 180px;
    font-size: 26px;
    font-weight: 700;
    color: var(--blue);
  }
  .contact-line {
    position: absolute;
    left: 300px;
    display: flex; align-items: center; gap: 14px;
    font-size: 17px;
    font-weight: 700;
    color: var(--orange);
  }
  .contact-line svg { width: 18px; height: 18px; }
  .contact-line--web { top: 236px; }
  .contact-line--mail { top: 270px; }
  /* Personal card */
  .card--personal { top: 812px; height: 322px; }
  .card--personal .logo { left: 34px; top: 60px; }
  .person__name {
    position: absolute;
    left: 332px; top: 132px;
    font-size: 19px;
    font-weight: 700;
    color: var(--orange);
  }
  .person__title {
    position: absolute;
    left: 332px; top: 162px;
    font-size: 13px;
    font-style: italic;
    color: var(--muted);
  }
  .person__details {
    position: absolute;
    left: 332px; top: 212px;
    display: grid;
    grid-template-columns: 58px auto;
    row-gap: 12px;
    font-size: 14px;
  }
  .person__details dt { color: var(--blue); }
  .person__details dd { color: var(--muted); }
</style>
</head>
<body>

<section class="card card--steps">
  <div class="steps">
    <div class="step">
      <div class="step__art step__art--drink" role="img" aria-label="Person sipping from a bottle of water"><span class="step__num">1</span></div>
      <p class="step__caption">Choose your bottled water (sip down 2 inches to create space)</p>
    </div>
    <div class="step">
      <div class="step__art step__art--charge" role="img" aria-label="Scoop of powder poured into the green Mix Comet"><span class="step__num">2</span></div>
      <p class="step__caption">Charge the Mix Comet (with your favorite powder)</p>
    </div>
    <div class="step">
      <div class="step__art step__art--release" role="img" aria-label="Mix Comet fitted on a bottle releasing powder into the water"><span class="step__num">3</span></div>
      <p class="step__caption">Release shot cap and Jet powder in</p>
    </div>
    <div class="step">
      <div class="step__art step__art--shake" role="img" aria-label="Hands shaking the bottle with the mixed drink"><span class="step__num">4</span></div>
      <p class="step__caption">Shake bottle, enjoy! (dispose of empty bottle thoughtfully)</p>
    </div>
  </div>
</section>

<section class="card card--general">
  <div class="logo"><span class="logo__dot"></span><span class="logo__name">Mix Comet</span></div>
  <p class="general__phone">415 382 6619</p>
  <p class="contact-line contact-line--web">
    <svg viewBox="0 0 20 20" fill="none" stroke="#1d4f9c" stroke-width="1.6"><circle cx="10" cy="10" r="8"/><ellipse cx="10" cy="10" rx="3.5" ry="8"/><line x1="2" y1="10" x2="18" y2="10"/></svg>
    www.mixcomet.com
  </p>
  <p class="contact-line contact-line--mail">
    <svg viewBox="0 0 20 20"><rect x="1" y="4" width="18" height="12" fill="#1d4f9c"/><polyline points="1,4 10,11 19,4" fill="none" stroke="#fff" stroke-width="1.5"/></svg>
    info@mixcomet.com
  </p>
</section>

<section class="card card--personal">
  <div class="logo"><span class="logo__dot"></span><span class="logo__name">Mix Comet</span></div>
  <p class="person__name">Rafe Dunmore</p>
  <p class="person__title">LL.b. / President</p>
  <dl class="person__details">
    <dt>Office:</dt><dd>415 382 6619</dd>
    <dt>Direct:</dt><dd>628 741 3085</dd>
    <dt>Email:</dt><dd>rafe@mixcomet.com</dd>
  </dl>
</section>

</body>
</html>
```